Teacher Grading Software Tri-Fold Brochure Design Project

Design a tri-fold brochure for MarkNimbus, a software-as-a-service web application that cuts teacher grading time by 30% to 70%. The purpose of the brochure is to get educators to sign up for a free trial of MarkNimbus. In addition to saving teachers valuable time, MarkNimbus helps teachers align their teaching with the Unified Benchmark standards, has a built-in rubric generator, and provides students with rubrics along with their assignments. It also provides comment reports that allow educators to see their students' strengths and weaknesses with the push of a button. More information on content is available at MarkNimbus's website, www.marknimbus.example.
We would like the brochure colors to mesh well with the logo and web site colors (www.marknimbus.example).
The design should highlight time and hassle savings, reporting, rubric generation and Unified Benchmark alignment.
Attached are the logo, two images we are willing to provide, if the designer uses them, and some marketing points., Design a tri-fold brochure for MarkNimbus, a software-as-a-service web application that cuts teacher grading time by 30% to 70%. The purpose of the brochure is to get educators to sign up for a free trial of MarkNimbus. In addition to saving teachers valuable time, MarkNimbus helps teachers align their teaching with the Unified Benchmark standards, has a built-in rubric generator, and provides students with rubrics along with their assignments. It also provides comment reports that allow educators to see their students' strengths and weaknesses with the push of a button. More information on content is available at MarkNimbus's website, www.marknimbus.example.
Attached are the logo, two images we are willing to provide, and some marketing points., Design a tri-fold brochure for MarkNimbus, a software-as-a-service web application that cuts teacher grading time by 30% to 70%. The purpose of the brochure is to get educators to sign up for a free trial of MarkNimbus. In addition to saving teachers valuable time, MarkNimbus helps teachers align their teaching with the Unified Benchmark standards, has a built-in rubric generator, and provides students with rubrics along with their assignments. It also provides comment reports that allow educators to see their students' strengths and weaknesses with the push of a button. More information on content is available at MarkNimbus's website, www.marknimbus.example.
Attached are the logo, two images we are willing to provide, and some marketing points.
Target Market(s)
School teachers, school principals, school district superintendents
Industry/Entity Type
Marketing
Look and feel

```html
<!DOCTYPE html>
<html lang="en">
<head>
<meta charset="utf-8">
<title>MarkNimbus Tri-Fold Brochure</title>
<link href="https://fonts.googleapis.com/css2?family=Oswald:wght@500&family=Raleway:wght@400;700&family=Open+Sans:wght@400;600&display=swap" rel="stylesheet">
<style>
:root{
  --teal:#1a8a78;
  --teal-dark:#10705f;
  --panel-teal:#138573;
  --blue:#1b6fc1;
  --purple:#8a3b9e;
  --brown:#8c1c0f;
  --petrol:#1b6f7c;
  --navy:#2c3b4f;
  --paper:#f2f2f2;
  --ink:#333;
  --white:#fff;
  --black:#111;
}
*{margin:0;padding:0;box-sizing:border-box}
html,body{width:1200px;height:1000px;overflow:hidden;background:var(--white)}
.canvas{position:relative;width:1200px;height:1000px;font-family:"Raleway",sans-serif;color:var(--ink)}
.brochure{position:absolute;left:15px;top:68px;width:1167px;height:897px;box-shadow:0 2px 8px rgba(0,0,0,.25)}
.panel{position:absolute;top:68px;height:890px}
.panel-inside{background:var(--paper)}
.panel-1{left:15px;width:387px}
.panel-2{left:402px;width:390px}
.panel-cover{left:792px;width:390px;background:linear-gradient(90deg,#fff 40%,#c9c9c9)}
.bottom-strip{position:absolute;left:15px;top:958px;width:1167px;height:7px;background:var(--black)}
.bottom-strip span{position:absolute;top:0;height:7px;background:#7fc9ba}
.abs{position:absolute}
.brand{position:absolute;font-family:"Raleway",sans-serif;font-weight:700;color:var(--navy);letter-spacing:-.5px}

.tag-heading{position:absolute;display:flex;align-items:center;font-family:"Oswald",sans-serif;font-weight:500;font-size:20px;line-height:30px;letter-spacing:-.2px;white-space:nowrap}
.tag-circle{flex:none;display:flex;align-items:center;border-radius:50%;color:var(--white)}
.tag-circle.end{justify-content:flex-end;padding-right:3px}
.tag-circle.center{justify-content:center}
.tag-circle.teal{background:var(--teal)}
.tag-circle.blue{background:var(--blue)}
.tag-rest{margin:0 3px}
.heading-line{position:absolute;font-family:"Oswald",sans-serif;font-weight:500;font-size:20px;line-height:30px;letter-spacing:-.2px;white-space:nowrap}

.body-copy{position:absolute;font-size:16.5px;line-height:23px;letter-spacing:-.15px;color:var(--ink)}
.badge{position:absolute;border-radius:50%;display:flex;align-items:center;justify-content:center;text-align:center;color:var(--white);font-family:"Open Sans",sans-serif;font-size:13px;line-height:22px;letter-spacing:-.3px}
.badge span{display:block}
.badge.cta{font-size:17px;line-height:25px;letter-spacing:0}
.photo{position:absolute}
.url{position:absolute;font-family:"Open Sans",sans-serif;font-weight:600;font-size:20px}
.ghost-words{position:absolute;left:792px;top:432px;width:390px;height:478px;overflow:hidden;font-family:"Open Sans",sans-serif;color:rgba(255,255,255,.1);white-space:nowrap}
.ghost-words span{position:absolute;display:block}
.cover-headline{position:absolute;right:40px;top:510px;text-align:right;font-family:"Oswald",sans-serif;font-weight:500;font-size:33px;line-height:50.5px;color:var(--white);text-shadow:1px 1px 2px rgba(0,0,0,.35)}
</style>
</head>
<body>
<div class="canvas">
  <div class="brochure"></div>

  <section class="panel panel-inside panel-1"></section>
  <section class="panel panel-inside panel-2"></section>
  <section class="panel panel-cover"></section>

  <svg class="abs" style="left:0;top:0" width="1200" height="1000" aria-hidden="true">
    <defs>
      <linearGradient id="fadeTeal" x1="0" x2="1"><stop offset="0" stop-color="#1a8a78" stop-opacity=".9"/><stop offset="1" stop-color="#1a8a78" stop-opacity="0"/></linearGradient>
      <linearGradient id="fadeBlue" x1="0" x2="1"><stop offset="0" stop-color="#1b6fc1" stop-opacity=".9"/><stop offset="1" stop-color="#1b6fc1" stop-opacity="0"/></linearGradient>
      <linearGradient id="fadePurple" x1="0" x2="1"><stop offset="0" stop-color="#8a3b9e" stop-opacity=".85"/><stop offset="1" stop-color="#8a3b9e" stop-opacity="0"/></linearGradient>
      <linearGradient id="fadeTeal2" x1="1" x2="0"><stop offset="0" stop-color="#1a8a78" stop-opacity=".9"/><stop offset="1" stop-color="#1a8a78" stop-opacity="0"/></linearGradient>
      <linearGradient id="fadeBlue2" x1="1" x2="0"><stop offset="0" stop-color="#1b6fc1" stop-opacity=".9"/><stop offset="1" stop-color="#1b6fc1" stop-opacity="0"/></linearGradient>
      <linearGradient id="fadePurple2" x1="1" x2="0"><stop offset="0" stop-color="#8a3b9e" stop-opacity=".85"/><stop offset="1" stop-color="#8a3b9e" stop-opacity="0"/></linearGradient>
    </defs>
    <polygon points="205,68 232,68 300,112 440,112 440,122 292,122" fill="url(#fadeTeal)"/>
    <polygon points="250,68 272,68 330,104 450,104 450,116 322,116" fill="url(#fadeBlue)" opacity=".8"/>
    <polygon points="300,68 330,68 390,110 470,110 470,150 380,150 330,100" fill="url(#fadePurple)" opacity=".6"/>
    <polygon points="790,548 700,548 650,510 625,510 690,560 790,560" fill="url(#fadeTeal2)"/>
    <polygon points="790,572 690,572 640,535 620,535 684,588 790,588" fill="url(#fadeBlue2)"/>
    <polygon points="790,600 700,600 650,560 630,560 690,628 790,628" fill="url(#fadePurple2)"/>
    <path d="M1172,68 C1160,170 1090,230 990,250 C1085,245 1160,190 1182,95 Z" fill="var(--teal)"/>
    <rect x="792" y="425" width="288" height="7" fill="#7fc9ba"/>
    <rect x="1080" y="425" width="102" height="7" fill="var(--black)"/>
    <rect x="792" y="432" width="390" height="478" fill="var(--panel-teal)"/>
    <rect x="792" y="910" width="390" height="48" fill="#d8d8d8"/>
  </svg>

  <div class="bottom-strip"><span style="left:180px;width:210px"></span><span style="left:580px;width:200px"></span><span style="left:930px;width:237px"></span></div>

  <!-- Panel 1 -->
  <div class="brand" style="left:45px;top:86px;font-size:27px">MarkNimbus</div>
  <div class="tag-heading" style="left:35px;top:132px;color:var(--teal)">
    <span class="tag-circle teal end" style="width:96px;height:96px">CAN BE</span>
    <span class="tag-rest">SECURELY USED</span>
  </div>
  <div class="heading-line" style="left:173px;top:198px;color:var(--teal)">ANYWHERE</div>
  <p class="body-copy" style="left:37px;top:238px;width:352px">Since MarkNimbus is entirely web-based, it saves its users from needing to carry around and keep track of large piles of paper. It uses the latest encryption technologies to ensure student confidentiality.</p>
  <div class="badge" style="left:35px;top:363px;width:100px;height:100px;background:var(--purple)"><span>grading<br>on any<br>device</span></div>
  <div class="badge" style="left:155px;top:363px;width:100px;height:100px;background:var(--brown)"><span>environmentally<br>concious</span></div>
  <div class="badge" style="left:275px;top:363px;width:100px;height:100px;background:var(--petrol)"><span>latest<br>encription<br>technologies</span></div>
  <p class="body-copy" style="left:37px;top:476px;width:352px">It also facilitates grading anywhere on nearly any device, including desktops, laptops, tablets, and even smartphones. MarkNimbus is also environmentally conscious: every three educators that switch to MarkNimbus save over a tree’s worth of paper per year. For an average high school, that is over ten trees per year!</p>
  <div class="photo" role="img" aria-label="Photo of a teacher with young students at desks in a classroom" style="left:37px;top:672px;width:344px;height:258px;background:linear-gradient(180deg,#d9d4c8 0%,#c9c0ad 35%,#8a7a62 60%,#b06a3a 100%)"></div>

  <!-- Panel 2 -->
  <div class="brand" style="left:433px;top:86px;font-size:27px">MarkNimbus</div>
  <div class="tag-heading" style="left:402px;top:124px;width:363px;justify-content:flex-end;color:var(--blue)">
    <span class="tag-rest" style="margin:0 1px 0 0">BRINGS GROUP</span>
    <span class="tag-circle blue center" style="width:94px;height:94px">TOGETHER</span>
  </div>
  <p class="body-copy" style="left:427px;top:240px;width:356px">Teachers and students are not the only people who can benefit from MarkNimbus. MarkNimbus is designed to be used by larger groups as well, such as departments, schools, districts, and school administrative units. Groups can run comment usage reports on a specific educator or on all of their educators as a whole, showing which techniques and instructors are most effective and making data-driven curriculum development a far easier task.</p>
  <div class="tag-heading" style="left:420px;top:578px;color:var(--blue)">
    <span class="tag-circle blue end" style="width:90px;height:90px">TRY OUT</span>
    <span class="tag-rest" style="margin-left:2px">- IT’S RISK-FREE</span>
  </div>
  <p class="body-copy" style="left:426px;top:674px;width:345px">Everyone has something to love about MarkNimbus. It benefits the Earth, it benefits teachers, and most importantly, it benefits students.</p>
  <p class="body-copy" style="left:427px;top:785px;width:175px">To fully appreciate MarkNimbus and what it can do for you</p>
  <div class="badge cta" style="left:608px;top:751px;width:148px;height:148px;background:var(--blue)"><span>sign up for a<br><b><i>risk-free trial</i></b><br>now!</span></div>
  <div class="url" style="left:402px;top:922px;width:390px;text-align:center;color:var(--blue)">www.marknimbus.example</div>

  <!-- Cover -->
  <div class="brand" style="left:822px;top:84px;font-size:44px">MarkNimbus</div>
  <div class="photo" role="img" aria-label="Photo of a tall stack of paper files" style="left:800px;top:170px;width:375px;height:255px;background:radial-gradient(ellipse 28% 48% at 40% 55%,#c9a86e,#a88a58 60%,rgba(200,200,200,0) 100%)"></div>
  <div class="ghost-words">
    <span style="left:40px;top:40px;font-size:56px;font-weight:600">Risk-free</span>
    <span style="left:10px;top:90px;font-size:44px">Create and Share</span>
    <span style="left:10px;top:140px;font-size:44px">Mange Rubrics</span>
    <span style="left:130px;top:215px;font-size:24px">Data-driven Instruction</span>
    <span style="left:30px;top:250px;font-size:44px">Saves your time</span>
    <span style="left:0;top:315px;font-size:38px">Brings Group Together</span>
    <span style="left:45px;top:370px;font-size:32px">Unified Benchmark Aligned</span>
    <span style="left:110px;top:400px;font-size:40px;color:rgba(255,255,255,.14)">Manages Revisions</span>
  </div>
  <h1 class="cover-headline">AN AFFORDABLE<br>WEB-BASED<br>GRADING APPLICATION<br>THAT SAVES EDUCATORS<br>HUNDREDS OF HOURS<br>PER YEAR</h1>
  <div class="url" style="left:792px;top:922px;width:390px;text-align:center;color:var(--teal-dark)">www.marknimbus.example</div>
</div>
</body>
</html>
```